A Real Estate Company Needs a Business Card Design

We need a business card design for a new company based in Boston MA called "Brellmont Real Estate LLC" we are a small company but we like a big corporate look, a simple, sleek, modern and progressive look. we would like the option of having a design that could include the real estate agents personal photo and also a design if the realtor decides not to have a photo. we do not have LOGO at this moment, please use any property look pic corporate with word" Brellmont Real Estate LLC" please see attached file as an example.

```html
<!DOCTYPE html>
<html lang="en">
<head>
<meta charset="utf-8">
<title>Brellmont Real Estate LLC – Business Card</title>
<link href="https://fonts.googleapis.com/css2?family=Roboto:wght@400;700&family=Open+Sans:wght@400;600&display=swap" rel="stylesheet">
<style>
  :root {
    --stage: #262626;
    --card-black: #0b0b0e;
    --card-black-soft: #2a2830;
    --brand-red: #e21b24;
    --brand-red-deep: #8e0f14;
    --paper: #ffffff;
    --ink-grey: #5a5a5a;
    --ink-dark: #3b3b3b;
    --photo-light: #c9b7a6;
    --photo-dark: #2f3340;
  }
  * { box-sizing: border-box; margin: 0; padding: 0; }
  html, body { width: 1200px; height: 738px; overflow: hidden; }
  body {
    background: radial-gradient(ellipse at 50% 30%, #3a3a3a 0%, var(--stage) 55%, #161616 100%);
    font-family: "Roboto", Arial, sans-serif;
    position: relative;
  }
  .card {
    position: absolute;
    top: 219px;
    width: 525px;
    height: 300px;
    border-radius: 4px;
    overflow: hidden;
    box-shadow: 0 18px 40px rgba(0,0,0,.55);
  }

  /* ---------- Back side ---------- */
  .card-back {
    left: 50px;
    background: linear-gradient(160deg, var(--card-black-soft) 0%, var(--card-black) 60%);
  }
  .card-back .sheen { position: absolute; inset: 0; }
  .card-back .brand {
    position: absolute;
    top: 108px; left: 0; right: 0;
    display: flex; justify-content: center; align-items: center; gap: 10px;
    color: var(--paper);
    font-weight: 700;
    font-size: 26px;
    letter-spacing: .5px;
  }
  .brand-mark {
    width: 16px; height: 16px;
    background: var(--brand-red);
    flex: none;
  }
  .card-back .band {
    position: absolute;
    left: 0; right: 0; top: 200px; height: 44px;
    background: linear-gradient(90deg, var(--brand-red-deep), var(--brand-red) 55%, var(--brand-red-deep));
  }
  .card-back .web {
    position: absolute;
    top: 258px; left: 0; right: 0;
    display: flex; justify-content: center; align-items: center; gap: 8px;
    font-family: "Open Sans", Arial, sans-serif;
    color: var(--paper);
    font-size: 15px;
    letter-spacing: 1px;
  }

  /* ---------- Front side ---------- */
  .card-front {
    left: 625px;
    background: var(--paper);
  }
  .card-front .top-band {
    position: absolute; left: 0; right: 0; top: 0; height: 82px;
    background: linear-gradient(90deg, var(--brand-red-deep) 0%, #b3141b 45%, var(--brand-red) 100%);
  }
  .card-front .person {
    position: absolute; right: 150px; top: 22px;
    text-align: right; color: var(--paper);
  }
  .person-name { font-weight: 700; font-size: 19px; }
  .person-role { font-size: 14px; margin-top: 8px; }
  .card-front .photo {
    position: absolute; right: 40px; top: 28px;
    width: 100px; height: 106px;
    border-radius: 9px;
    border: 3px solid var(--paper);
    background: linear-gradient(180deg, var(--photo-light) 0%, #a08f80 55%, var(--photo-dark) 100%);
    box-shadow: 0 1px 4px rgba(0,0,0,.25);
  }
  .card-front .brand {
    position: absolute; left: 32px; top: 142px;
    display: flex; align-items: center; gap: 10px;
    color: var(--ink-dark);
    font-weight: 700; font-size: 21px;
  }
  .card-front .contacts {
    position: absolute; right: 22px; top: 144px; width: 136px;
    text-align: center;
    font-family: "Open Sans", Arial, sans-serif;
    color: var(--ink-grey);
    font-size: 11px;
    line-height: 1.2;
  }
  .contacts .icon { display: block; margin: 0 auto 4px; }
  .contacts .social-dot {
    display: block; width: 10px; height: 10px; border-radius: 50%;
    background: var(--brand-red); margin: 8px auto 4px;
  }
  .card-front .footer {
    position: absolute; left: 0; right: 0; bottom: 0; height: 78px;
    background: linear-gradient(180deg, #1a191d 0%, var(--card-black) 100%);
    color: var(--paper);
    font-family: "Open Sans", Arial, sans-serif;
    font-size: 12.5px;
  }
  .footer .line { position: absolute; display: flex; align-items: center; gap: 7px; white-space: nowrap; }
  .footer .address { left: 62px; top: 12px; }
  .footer .email { left: 34px; top: 34px; }
  .footer .website { left: 268px; top: 48px; }
</style>
</head>
<body>

  <section class="card card-back" aria-label="Business card, back">
    <svg class="sheen" width="525" height="300" viewBox="0 0 525 300" aria-hidden="true">
      <path d="M0 95 C150 55 330 60 525 110 L525 0 L0 0 Z" fill="rgba(255,255,255,0.06)"/>
    </svg>
    <div class="brand"><span class="brand-mark"></span>Brellmont Real Estate LLC</div>
    <div class="band"></div>
    <div class="web">
      <svg width="14" height="14" viewBox="0 0 14 14" aria-hidden="true">
        <circle cx="7" cy="7" r="6" fill="none" stroke="#fff" stroke-width="1.2"/>
        <path d="M1 7h12M7 1c-3 3-3 9 0 12M7 1c3 3 3 9 0 12" fill="none" stroke="#fff" stroke-width="1"/>
      </svg>
      www.yourwebaddresshere.com
    </div>
  </section>

  <section class="card card-front" aria-label="Business card, front">
    <div class="top-band"></div>
    <div class="person">
      <div class="person-name">Mr. Daniel Harlow</div>
      <div class="person-role">Marketing Manager</div>
    </div>
    <div class="photo" role="img" aria-label="Agent portrait photo"></div>

    <div class="brand"><span class="brand-mark"></span>Brellmont Real Estate LLC</div>

    <div class="contacts">
      <svg class="icon" width="9" height="14" viewBox="0 0 9 14" aria-hidden="true">
        <rect x="0.5" y="0.5" width="8" height="13" rx="1.5" fill="var(--brand-red)"/>
        <rect x="2" y="2" width="5" height="5" fill="#fff"/>
        <circle cx="4.5" cy="10.5" r="1" fill="#fff"/>
      </svg>
      000.123.1234
      <span class="social-dot"></span>
      Brellmont Real Estate LLC
    </div>

    <div class="footer">
      <div class="line address">
        <svg width="14" height="12" viewBox="0 0 14 12" aria-hidden="true">
          <path d="M7 0 L14 6 H12 V12 H8.5 V8 H5.5 V12 H2 V6 H0 Z" fill="#fff"/>
        </svg>
        Your Address here, City ABC, State 123 Loram Ipsum Newyork.
      </div>
      <div class="line email">
        <svg width="13" height="9" viewBox="0 0 13 9" aria-hidden="true">
          <rect x="0.5" y="0.5" width="12" height="8" fill="#fff"/>
          <path d="M0.5 0.5 L6.5 5 L12.5 0.5" fill="none" stroke="#111" stroke-width="1"/>
        </svg>
        info@yourwebaddresshere.com
      </div>
      <div class="line website">
        <svg width="13" height="13" viewBox="0 0 14 14" aria-hidden="true">
          <circle cx="7" cy="7" r="6" fill="none" stroke="#fff" stroke-width="1.2"/>
          <path d="M1 7h12M7 1c-3 3-3 9 0 12M7 1c3 3 3 9 0 12" fill="none" stroke="#fff" stroke-width="1"/>
        </svg>
        www.yourwebaddresshere.com
      </div>
    </div>
  </section>

</body>
</html>
```